Home Renovation Business needs a logo and business card design

I need a logo design for my home renovation company. I work hard to provide quality work for a fair price. I want a clean design that has something to make it pop and catch the eye. It should have somewhat of a modern feel to it. You can check out my website at www.kolbrenhomes.com to see some examples of the type of work I do.
Updates

Hi Everyone,

For some reason, not all my information was posted. I would like the following contact information included in the design:

Phone: 365.412.7958        Email: tkeswick@orvale.ca        Website: www.kolbrenhomes.com

Also, if you would like to include a list of the services I offer, then I'd like the card to be double sided. I provide the following services: Full kitchen, basement and bathroom renovations. Tile, laminate and hardwood installation. Decks, fences and sheds. Windows and doors.

Industry/Entity Type

Business

Requirements
Must have
• I want the following information listed on the card:
• TK Renovations
• Tom Keswickle
• 365.412.7958
• tkeswick@orvale.ca
• www.kolbrenhomes.com
Nice to have
• If you want you could also include the list of services I provide. If you include this list feel free to make the card double sided.
• Kitchen, bathroom and basement renovations
• Flooring installation
• Decks, fences and sheds
• Windows and doors
• I am not 100% sure if I want to include this on the card or not.

```html
<!DOCTYPE html>
<html lang="en">
<head>
<meta charset="utf-8">
<title>TK Renovations – Business Card</title>
<link rel="stylesheet" href="https://fonts.googleapis.com/css2?family=Oswald:wght@700&family=Arimo:wght@400;700&display=swap">
<style>
  :root {
    --orange: #e9a84b;
    --charcoal: #2b2b2c;
    --charcoal-soft: #3d3d3e;
    --slate: #6c6c6e;
    --ink: #111111;
    --white: #ffffff;
    --page: #ffffff;
  }
  * { box-sizing: border-box; margin: 0; padding: 0; }
  html, body {
    width: 1200px; height: 353px; overflow: hidden;
    background: var(--page);
    font-family: "Arimo", Arial, sans-serif;
  }
  .sheet { position: relative; width: 1200px; height: 353px; }
  .card {
    position: absolute; top: 8px;
    width: 575px; height: 337px;
    background: var(--orange);
    overflow: hidden;
  }
  .card--front { left: 10px; }
  .card--back { left: 614px; }
  .card__band { position: absolute; inset: 0; width: 100%; height: 100%; }

  .brand-name {
    font-family: "Oswald", "Arial Narrow", sans-serif;
    font-weight: 700;
    letter-spacing: 0.5px;
    line-height: 1;
    white-space: nowrap;
  }
  .front__brand { position: absolute; left: 178px; top: 18px; }
  .front__brand .brand-name { font-size: 52px; color: var(--ink); }
  .front__url {
    margin-top: 4px; margin-left: 36px;
    font-size: 21px; font-weight: 700; color: var(--ink);
  }
  .contact {
    position: absolute; left: 18px; top: 246px;
    color: var(--white); font-size: 18px; line-height: 21px;
  }
  .contact__name { text-transform: uppercase; }

  .services { list-style: none; position: absolute; inset: 0; }
  .services__item {
    position: absolute;
    display: flex; align-items: center; gap: 8px;
    font-size: 17px; color: var(--ink); white-space: nowrap;
  }
  .services__item::before {
    content: ""; width: 7px; height: 7px; background: var(--charcoal);
  }
  .back__brand { position: absolute; left: 14px; top: 258px; color: var(--white); }
  .back__brand .brand-name { font-size: 30px; }
  .back__url { margin-top: 2px; font-size: 13px; font-weight: 700; }
</style>
</head>
<body>
<main class="sheet">
  <section class="card card--front" aria-label="Card front">
    <svg class="card__band" viewBox="0 0 575 337" aria-hidden="true">
      <defs>
        <linearGradient id="charcoalFront" x1="0" y1="0" x2="1" y2="1">
          <stop offset="0" stop-color="var(--charcoal-soft)"/>
          <stop offset="1" stop-color="var(--charcoal)"/>
        </linearGradient>
      </defs>
      <polygon points="0,0 108,0 302,337 0,337" fill="url(#charcoalFront)"/>
      <polygon points="108,0 128,0 322,337 302,337" fill="var(--slate)"/>
    </svg>
    <div class="front__brand">
      <div class="brand-name">TK RENOVATIONS</div>
      <div class="front__url">www.kolbrenhomes.com</div>
    </div>
    <div class="contact">
      <p class="contact__name">Tom Keswickle</p>
      <p>phone: 365.412.7958</p>
      <p>email: tkeswick@orvale.ca</p>
    </div>
  </section>

  <section class="card card--back" aria-label="Card back">
    <svg class="card__band" viewBox="0 0 575 337" aria-hidden="true">
      <defs>
        <linearGradient id="charcoalBack" x1="0" y1="0" x2="1" y2="1">
          <stop offset="0" stop-color="var(--charcoal-soft)"/>
          <stop offset="1" stop-color="var(--charcoal)"/>
        </linearGradient>
      </defs>
      <polygon points="0,0 70,0 245,337 0,337" fill="url(#charcoalBack)"/>
      <polygon points="70,0 90,0 265,337 245,337" fill="var(--slate)"/>
    </svg>
    <ul class="services">
      <li class="services__item" style="left:112px; top:26px;">Kitchen, basement and bathroom renovations</li>
      <li class="services__item" style="left:124px; top:78px;">Tile, laminate and hardwood installation</li>
      <li class="services__item" style="left:166px; top:130px;">Deck, fence and shed construction</li>
      <li class="services__item" style="left:206px; top:183px;">Window and door repair</li>
    </ul>
    <div class="back__brand">
      <div class="brand-name">TK RENOVATIONS</div>
      <div class="back__url">www.kolbrenhomes.com</div>
    </div>
  </section>
</main>
</body>
</html>
```